LVM IT Solutions Provider

Please read attached documentation completely before beginning Project. Thank you!

Mark Forge Project Requirements

Thank you for your interest in this design contest. We are always welcome to questions and are looking forward to seeing what you can come up with.

The logo is located on the current site homepage http://www.lumavex.com/

Bootstrap

We work on a Bootstrap platform with our custom built CMS. We require all designs to be

sized accordingly with the bootstrap grid system found here: http://getframelyn.com/css/#grid

Start of Competition Requirements

At the start of a competition, we are looking for general Home Page Design concepts and interior page design concepts as well.

HOME PAGE DESIGN

Any changes requested by the client in the original designs

Responsive Tablet View (using standard bootstrap media queries, we need to see an

example of a tablet size home page view)

Responsive Phone View (using standard bootstrap media queries, we need to see an

example of a phone size home page view)

INTERIOR PAGE DESIGN

These pages are general content pages. Our CMS allows for the creation of unlimited

pages and gives the client control of adding them. Interior Page Designs can be built

with 1 column, 2 columns (either right side bar or left sidebar)

Examples of buttons and button states,

Examples of drop down menus

Examples of H1 through H5 plus body copy

We uploaded a clean logo to use on the project. Thank you.

We added a updated Creative Brief document to help out. Please take a look thanks!

```html
<!DOCTYPE html>
<html lang="en">
<head>
<meta charset="utf-8">
<title>LVM — Lumavex Vector Methods</title>
<link href="https://fonts.googleapis.com/css2?family=Oswald:wght@500;700&family=Arimo:wght@400&display=swap" rel="stylesheet">
<style>
:root{
  --blue:#0b55a0;
  --yellow:#f0b92e;
  --ink:#333333;
  --muted:#666666;
  --rule:#e2e2e2;
  --footer:#f4f4f4;
  --white:#ffffff;
}
*{margin:0;padding:0;box-sizing:border-box}
html,body{width:970px;height:1200px;overflow:hidden;background:var(--white)}
body{position:relative;font-family:"Arimo",Arial,sans-serif;color:var(--ink)}
.abs{position:absolute}
.display{font-family:"Oswald","Arial Narrow",sans-serif;font-weight:700;letter-spacing:-.3px}

/* header */
.brand{left:101px;top:26px;display:flex;align-items:center;gap:8px}
.brand-mark{width:14px;height:14px;border-radius:50%;background:var(--yellow)}
.brand-name{font-family:"Oswald",sans-serif;font-weight:700;font-size:34px;color:var(--blue);line-height:1}
.brand-sub{left:101px;top:64px;font-size:7px;color:var(--blue);letter-spacing:.5px}
.nav-home{left:319px;top:0;width:69px;height:92px;background:var(--yellow)}
.nav-item{top:38px;font-size:14.5px;color:var(--blue)}
.nav-item.active{color:var(--white);left:319px;width:69px;text-align:center}
.hiring{left:747px;top:31px;width:106px;height:34px;background:var(--yellow);border-radius:3px;color:var(--white);font-size:14px;display:flex;align-items:center;justify-content:center;gap:6px}

/* hero */
.hero-photo{left:0;top:92px;width:970px;height:365px;background:linear-gradient(100deg,#cfd3d6 0%,#e9ecee 40%,#dfe4e8 70%,#c9d0d6 100%)}
.hero-panel{left:101px;top:92px;width:218px;height:365px;background:var(--blue);color:var(--white);padding:64px 18px 0}
.hero-panel h1{font-size:16px;line-height:19px;margin-bottom:24px}
.hero-panel p{font-size:11px;line-height:19.4px}
.hero-tag{right:102px;top:354px;text-align:right;font-size:23.5px;line-height:28px;color:#0a2c52}
.dots{left:812px;top:434px;display:flex;gap:4px}
.dots span{width:11px;height:11px;border-radius:50%;background:var(--white)}
.dots span:first-child{background:var(--blue)}

/* band */
.band{left:0;top:457px;width:970px;height:81px;background:var(--yellow)}
.band-title{left:140px;top:489px;font-size:14px;color:var(--white)}
.band-text{left:313px;top:469px;width:545px;font-size:10.5px;line-height:19.4px;color:var(--white)}

/* services */
.svc{width:250px}
.svc-head{display:flex;align-items:center;gap:10px;height:24px}
.svc-head h2{font-size:14.5px;color:var(--blue);font-family:"Oswald",sans-serif;font-weight:700;letter-spacing:-.3px;white-space:nowrap}
.svc ul{list-style:none;margin-top:14px}
.svc li{position:relative;padding-left:34px;font-size:11px;line-height:19.4px}
.svc li::before{content:"›";position:absolute;left:10px;top:0;font-size:13px}
.svc.tech{width:215px}
.svc.sim{width:265px}
.svc.sim li{padding-left:26px}
.vrule{width:1px;background:var(--rule)}
.hrule{left:101px;top:755px;width:768px;height:1px;background:var(--rule)}

/* footer */
.footer{left:0;top:943px;width:970px;height:257px;background:var(--footer)}
.foot-head{font-family:"Oswald",sans-serif;font-weight:700;font-size:11px;color:var(--muted);top:972px}
.foot-list{list-style:none;font-size:11px;color:var(--muted)}
.links li{line-height:30.7px}
.contact li{line-height:22.6px}
.badge{background:#d7dbe0;border-radius:4px}
.intranet{left:784px;top:993px;display:flex;align-items:center;gap:4px;font-size:11px;color:#222}
.intranet span.ring{width:36px;height:36px;border:1.5px solid #4a4ae0;border-radius:50%}
.social{top:1063px;width:29px;height:29px;border-radius:50%;border:1.5px solid var(--blue)}
.copy{left:0;width:970px;top:1151px;text-align:center;font-size:11px;color:var(--muted)}
</style>
</head>
<body>

<header>
  <div class="abs brand"><span class="brand-name">LVM</span><span class="brand-mark"></span></div>
  <div class="abs brand-sub">LUMAVEX VECTOR METHODS</div>
  <div class="abs nav-home"></div>
  <nav class="display">
    <span class="abs nav-item active">Home</span>
    <span class="abs nav-item" style="left:395px">About LVM</span>
    <span class="abs nav-item" style="left:474px">Divisions</span>
    <span class="abs nav-item" style="left:549px">Products/Services</span>
    <span class="abs nav-item" style="left:676px">Contact Us</span>
    <span class="abs hiring">WE'RE HIRING
      <svg width="10" height="8" viewBox="0 0 10 8"><path d="M1 2l4 4 4-4" fill="none" stroke="#fff" stroke-width="2"/></svg>
    </span>
  </nav>
</header>

<section>
  <div class="abs hero-photo" role="img" aria-label="Scientist in safety goggles and mask examining a test tube in a lab"></div>
  <div class="abs hero-panel">
    <h1 class="display">Welcome To Lumavex Vector Methods</h1>
    <p>Since 1988, Lumavex Vector Methods has been providing innovative and cost-effective products and services to customers worldwide. We are a vital source for leading-edge technology solutions that help our customers respond to opportunities faster, achieve more from their operations, and exceed their requirements.</p>
  </div>
  <p class="abs hero-tag">Technology solutions for national<br>defense and global security</p>
  <div class="abs dots"><span></span><span></span><span></span><span></span></div>
</section>

<section>
  <div class="abs band"></div>
  <h2 class="abs band-title display">LVM PRODUCT OR SERVICE</h2>
  <p class="abs band-text">LVM provides the U.S. government and other customers with a vast array of quality products and services. At the core of LVM's capabilities are highly skilled engineers and scientists that apply their expertise on the entire product life cycle including requirement definition, design, integration, test, and long-term support.</p>
</section>

<main>
  <div class="abs svc" style="left:97px;top:589px">
    <div class="svc-head"><svg width="24" height="24" viewBox="0 0 24 24"><circle cx="12" cy="12" r="11" fill="#f0b92e"/><path d="M1 12h22M12 1v22M4 6h16M4 18h16" stroke="#fff" stroke-width="1.4"/></svg><h2>COMMUNICATIONS &amp; NETWORKING</h2></div>
    <ul><li>MeshPath®<br>Wireless Ad Hoc Routing Protocol</li><li>SwiftLink® 1000C</li><li>Compact Networked Spectrum Watch and Engineering Control Suite</li></ul>
  </div>
  <div class="abs vrule" style="left:355px;top:592px;height:111px"></div>
  <div class="abs svc tech" style="left:368px;top:587px">
    <div class="svc-head"><svg width="22" height="24" viewBox="0 0 22 24"><path d="M3 22l4-10 8 6z" fill="#f0b92e"/><path d="M10 6a6 6 0 0 1 6 6M10 2a10 10 0 0 1 10 10" fill="none" stroke="#f0b92e" stroke-width="2"/></svg><h2>TECHNOLOGY INSERTION</h2></div>
    <ul style="margin-top:16px"><li>K-20 Sealed Panel Multi-Function Color Display</li></ul>
  </div>
  <div class="abs vrule" style="left:614px;top:592px;height:111px"></div>
  <div class="abs svc sim" style="left:626px;top:585px">
    <div class="svc-head"><svg width="18" height="24" viewBox="0 0 18 24"><path d="M9 1c4 4 5 9 4 16H5C4 10 5 5 9 1z" fill="#f0b92e"/><path d="M5 14l-4 6h4zM13 14l4 6h-4z" fill="#f0b92e"/><circle cx="9" cy="9" r="2" fill="#fff"/></svg><h2>SIMULATION &amp; TEST</h2></div>
    <ul style="margin-top:18px"><li>Adaptive Radar Scene Generator</li><li>GPS Jammer</li><li>Multi-Spectral Stimulator</li><li>Threat Field Emulation System</li><li>Virtual Air Defense Trainer (VADT)</li></ul>
  </div>

  <div class="abs hrule"></div>

  <div class="abs svc" style="left:105px;top:809px">
    <div class="svc-head"><svg width="18" height="22" viewBox="0 0 18 22"><path d="M4 10V6a5 5 0 0 1 10 0v4" fill="none" stroke="#f0b92e" stroke-width="2.5"/><rect x="1" y="10" width="16" height="12" rx="1" fill="#f0b92e"/></svg><h2>INTELLIGENCE &amp; SECURITY</h2></div>
    <ul><li style="padding-left:26px">Cryptologic &amp; Threat Warning Systems</li><li style="padding-left:26px">Intelligence Systems</li></ul>
  </div>
  <div class="abs vrule" style="left:355px;top:812px;height:110px"></div>
  <div class="abs svc" style="left:366px;top:808px">
    <div class="svc-head"><svg width="18" height="22" viewBox="0 0 18 22"><path d="M5 6a8 8 0 1 0 8 0" fill="none" stroke="#f0b92e" stroke-width="2.5"/><path d="M9 2v9" stroke="#f0b92e" stroke-width="2.5"/></svg><h2>AUTOMATION SYSTEMS</h2></div>
    <ul><li>Automation Systems</li></ul>
  </div>
  <div class="abs vrule" style="left:614px;top:812px;height:110px"></div>
  <div class="abs svc" style="left:623px;top:809px">
    <div class="svc-head"><svg width="24" height="18" viewBox="0 0 24 18"><path d="M5 17a4 4 0 0 1 0-8 6 6 0 0 1 11-3 5 5 0 0 1 3 11z" fill="#f0b92e"/></svg><h2>CLOUD SOLUTIONS</h2></div>
    <ul><li>Cloud Solutions for Nimbus Ledger</li></ul>
  </div>
</main>

<footer>
  <div class="abs footer"></div>
  <h3 class="abs foot-head" style="left:150px">QUICK LINKS</h3>
  <ul class="abs foot-list links" style="left:150px;top:1006px"><li>Home</li><li>About LVM</li><li>Divisions</li><li>Products/ Services</li></ul>
  <h3 class="abs foot-head" style="left:392px">CONTACT US</h3>
  <ul class="abs foot-list contact" style="left:392px;top:1010px"><li>(555) 214-7730,</li><li>1480 Cedar Bend Avenue,</li><li>Suite 210 North Harlow,</li><li>&nbsp;GA 30412</li></ul>
  <div class="abs badge" style="left:668px;top:982px;width:43px;height:47px"></div>
  <div class="abs badge" style="left:718px;top:980px;width:58px;height:51px;border-radius:50%"></div>
  <div class="abs intranet">intranet<span class="ring"></span></div>
  <span class="abs social" style="left:663px"></span>
  <span class="abs social" style="left:697px"></span>
  <span class="abs social" style="left:731px;border-color:#3aa0d8"></span>
  <p class="abs copy">Copyright 2014. All rights reserved. © Lumavex Vector Methods</p>
</footer>

</body>
</html>
```